Web Design Project for Industrial Hemp

I'm launching a new company to grow Industrial Hemp and then to set up a manufacturing facility to process the crop each and every year. We require a complete end to end brand and livery suite and we will start with a web presence. We want to appeal to (a) Investors, Employees, Farmers, and consumers so as to engage with all our stakeholders. We want to create a whole new industry that becomes a game changer for environmentally friendly crop production. Hemp is gaining in popularity and credibility across the world!

Target Market(s)

Farmers to produce, Manufacturers who will purchase the raw materials, Investors who will invest in the project, Consumers who will buy Hemp Products

Industry/Entity Type

Industry

Requirements
Must have
• Environmentally Friendly
Carbon Neutral/Positive
Game Changer
Multi-Use Crop
50,000 products can be made from Hemp
Should not have
• Should avoid its relationship with cannabis but not ignore it! When the regulatory bodies acknowledge the benefits of cannabanoids, they will start to legalise the production of cannabis for sale on prescription

```html
<!DOCTYPE html>
<html lang="en">
<head>
<meta charset="utf-8">
<title>Verdant Field Fibres — Industrial Hemp</title>
<link href="https://fonts.googleapis.com/css2?family=Lilita+One&family=Oswald:wght@300;400;700&display=swap" rel="stylesheet">
<style>
:root{
  --page:#efede8;
  --white:#ffffff;
  --green-dark:#3a8a0e;
  --green-nav:#4fa620;
  --green-tile:#a6cf3b;
  --green-head:#3d8d13;
  --text:#333333;
  --footer-bg:#e5e1d3;
  --brown:#7a5c0c;
  --gold:#c4a84a;
  --gold-light:#d8cf9e;
  --field:#dcd6c0;
  --rule:#d5d2ca;
}
*{box-sizing:border-box;margin:0;padding:0}
html,body{width:689px;height:1200px;overflow:hidden}
body{position:relative;background:var(--page);font-family:Arial,Helvetica,sans-serif;color:var(--text)}
.abs{position:absolute}
.header{left:0;top:0;width:689px;height:72px;background:var(--white);z-index:2}
.brand{left:20px;top:10px;width:118px;height:54px}
.brand-mark{left:48px;top:0;width:22px;height:22px;border-radius:50%;background:var(--green-tile)}
.brand-name{left:0;top:29px;width:118px;height:18px;background:var(--green-dark);color:var(--white);font-family:'Oswald',sans-serif;font-weight:400;font-size:10px;line-height:18px;text-align:center;letter-spacing:.3px}
.search{left:523px;top:22px;width:155px;height:24px;border-radius:7px;background:var(--green-tile)}
.search span{position:absolute;left:11px;top:6px;font-size:8px;color:#3c6a10}
.search-btn{position:absolute;right:4px;top:3px;width:20px;height:18px;border-radius:5px;background:var(--green-dark)}
.nav{left:155px;top:54px;width:524px;height:29px;background:var(--green-nav);display:flex;z-index:3}
.nav a{flex:1;color:var(--white);text-decoration:none;font-family:'Oswald',sans-serif;font-weight:300;font-size:13px;line-height:29px;text-align:center;border-right:1px solid #3f8c16;white-space:nowrap}
.nav a:last-child{border-right:none}
.hero{left:0;top:72px;width:689px;height:227px;background:linear-gradient(180deg,#5f9a2a,#4d8a22 40%,#7bb53d 75%,#3f7a1a);z-index:1}
.headline{left:0;top:306px;width:689px;text-align:center;color:var(--green-dark);white-space:nowrap;line-height:46px}
.headline .big{font-family:'Oswald',sans-serif;font-weight:700;font-size:37px;letter-spacing:-.5px}
.headline .small{font-family:'Lilita One',sans-serif;font-size:21px;margin-left:5px}
.tiles{left:7px;top:358px;width:674px;height:149px;display:flex;gap:1px;background:#d9ecb0}
.tile{flex:1;background:var(--green-tile);position:relative}
.tile .photo{position:absolute;left:7px;top:7px;right:7px;height:98px}
.tile .label{position:absolute;left:0;right:0;bottom:8px;text-align:center;color:var(--white);font-family:'Oswald',sans-serif;font-size:20px}
.feature{top:563px;width:158px}
.feature h3,.section-title{font-family:'Lilita One',sans-serif;color:var(--green-head);font-weight:400;white-space:nowrap}
.feature h3{font-size:11.5px}
.section-title{font-size:12px}
.feature p{font-size:8.2px;line-height:10.3px;margin-top:7px}
.feature svg{float:left;margin:0 8px 2px 2px}
.rule{left:0;top:689px;width:689px;height:1px;background:var(--rule)}
.welcome-photo{left:18px;top:760px;width:272px;height:133px;border:2px solid var(--white);background:linear-gradient(180deg,#4f86c6 0%,#86b3de 35%,#6a7d5c 45%,#3d6d9a 58%,#a56a35 75%,#8a5a2e)}
.welcome-text{left:18px;top:901px;width:280px;font-size:8.3px;line-height:10.3px}
.services{left:331px;top:757px;list-style:none}
.services li{font-size:8.4px;height:21.1px;padding-left:14px;position:relative;white-space:nowrap}
.services li::before{content:"»";position:absolute;left:0;top:-3px;font-size:12px;color:#555;font-weight:bold}
.news-item{left:515px;width:165px}
.date{position:absolute;left:0;top:0;width:24px;text-align:center}
.date b{display:block;width:24px;height:24px;border-radius:50%;border:2px solid var(--gold);background:var(--gold);color:var(--white);font-family:'Oswald',sans-serif;font-size:12px;line-height:20px;box-shadow:inset 0 0 0 1px var(--white)}
.date i{font-style:normal;font-size:8px;color:var(--brown);font-weight:bold;display:block;margin-top:3px}
.news-body{position:absolute;left:40px;top:2px;width:125px}
.news-body h4{font-size:8.6px}
.news-body p{font-size:7.4px;line-height:9.4px;color:#666;margin-top:4px}
.news-body a{font-size:7.4px;color:var(--gold);font-weight:bold;text-decoration:none}
.dotted{left:518px;width:156px;border-top:1px dotted var(--gold)}
.more{left:515px;top:908px;width:57px;height:22px;border-radius:5px;background:var(--gold);border:2px solid var(--gold-light);color:var(--white);font-family:'Oswald',sans-serif;font-weight:700;font-size:10px;line-height:18px;text-align:center;white-space:nowrap;letter-spacing:-.2px}
.footer{left:0;top:992px;width:689px;height:208px;background:var(--footer-bg)}
.footer-title{font-family:'Lilita One',sans-serif;color:var(--brown);font-size:13px;font-weight:400}
.foot-links{list-style:none;font-size:8.2px;line-height:12.8px;color:#9a7a1a}
.field{left:240px;width:173px;height:20px;border-radius:6px;background:var(--field);font-size:7.4px;font-weight:bold;color:#6a5a30;padding:6px 0 0 15px}
.send{left:365px;top:1162px;width:48px;height:20px;border-radius:3px;background:var(--gold);color:#5a4408;font-size:8px;font-weight:bold;text-align:center;line-height:20px}
.social{left:524px;top:1047px;display:flex;gap:6px}
.social span{width:20px;height:20px;border-radius:50%;background:var(--gold)}
.sub-note{left:524px;top:1077px;font-size:7.2px;line-height:9px;color:#5a4408;font-weight:bold}
.sub-field{left:523px;top:1101px;width:130px;height:19px;border-radius:10px;background:var(--gold);color:var(--white);font-size:7.4px;line-height:19px;padding-left:11px}
.sub-now{left:525px;top:1130px;font-size:7.6px;font-weight:bold;color:#5a4408}
.phone{left:522px;top:1151px;display:flex;align-items:center;gap:8px;font-family:'Oswald',sans-serif;font-weight:300;font-size:19px;color:var(--gold)}
</style>
</head>
<body>

<header class="abs header">
  <div class="abs brand">
    <span class="abs brand-mark"></span>
    <div class="abs brand-name">VERDANT FIELD FIBRES</div>
  </div>
  <div class="abs search"><span>Search ...</span>
    <div class="search-btn"><svg width="20" height="18" viewBox="0 0 20 18"><circle cx="9" cy="8" r="3.5" fill="none" stroke="#fff" stroke-width="1.5"/><line x1="11.5" y1="10.5" x2="15" y2="14" stroke="#fff" stroke-width="2"/></svg></div>
  </div>
</header>

<div class="abs hero" role="img" aria-label="Field of tall green hemp plants"></div>

<nav class="abs nav">
  <a href="#">HOME</a><a href="#">ABOUT US</a><a href="#">PRODUCTION</a><a href="#">INVESTORS</a><a href="#">PRODUCTS</a><a href="#">CONTACT US</a>
</nav>

<h1 class="abs headline"><span class="big">50,000 PRODUCTS</span><span class="small">CAN BE MADE FROM HEMP</span></h1>

<section class="abs tiles">
  <div class="tile"><div class="photo" role="img" aria-label="Bowl of hemp seed granola" style="background:linear-gradient(180deg,#b07a48,#e8e2d8)"></div><div class="label">FOOD</div></div>
  <div class="tile"><div class="photo" role="img" aria-label="Fuel nozzle filling a car" style="background:linear-gradient(135deg,#2e2e6a,#8a8ab0 55%,#d9d4cc)"></div><div class="label">FUEL</div></div>
  <div class="tile"><div class="photo" role="img" aria-label="Bundles of raw hemp fibre" style="background:linear-gradient(180deg,#8a8a70,#c8c6b0)"></div><div class="label">FIBER</div></div>
  <div class="tile"><div class="photo" role="img" aria-label="Hemp oil in a tin" style="background:radial-gradient(circle at 45% 55%,#d86a10,#5a2c10 60%,#2a2a2a)"></div><div class="label">OIL</div></div>
  <div class="tile"><div class="photo" role="img" aria-label="Sheets of hemp paper" style="background:linear-gradient(135deg,#d9c3a0,#c4a878)"></div><div class="label">PAPER</div></div>
  <div class="tile"><div class="photo" role="img" aria-label="Folded hemp textile" style="background:linear-gradient(180deg,#4a4a4a,#a8aaa8 60%,#6a6a6a)"></div><div class="label">TEXTILES</div></div>
</section>

<div class="abs feature" style="left:12px">
  <h3>ENVIRONMENTAL FRIENDLY</h3>
  <p><svg width="28" height="28" viewBox="0 0 28 28"><path d="M14 26V14M14 14C8 14 5 9 6 5c5 0 8 4 8 9zM14 12c1-5 5-8 11-8-1 6-5 9-11 8z" fill="#4fa620" stroke="#4fa620" stroke-width="1.2"/><ellipse cx="14" cy="26" rx="9" ry="1.5" fill="#4fa620"/></svg>Donec hendrerit, felis in aliquet sodales, leo neque posuere arcu, sit amet sodales libero augue eget libero. Proin consequat odio eget ligula lobortis sodales. Suspendisse potenti.</p>
</div>
<div class="abs feature" style="left:186px">
  <h3>CARBON NEUTRAL POSITIVE</h3>
  <p><span style="float:left;font-family:'Oswald',sans-serif;color:#8cc63f;font-size:22px;line-height:24px;margin-right:8px">CO<sup style="font-size:10px">2</sup></span>Vntur magni dolores eoquie voluptate msequi nesciunt. Nique porroisquam esti dolorem ipsumquia dolorsita onsectet. Ferpisci velit, sed quia non numquam eiumodi tempora.</p>
</div>
<div class="abs feature" style="left:354px">
  <h3>GAME CHANGER</h3>
  <p><svg width="32" height="28" viewBox="0 0 32 28"><rect x="3" y="18" width="4" height="9" fill="#6bb02a"/><rect x="10" y="14" width="4" height="13" fill="#6bb02a"/><rect x="17" y="16" width="4" height="11" fill="#6bb02a"/><rect x="24" y="10" width="4" height="17" fill="#6bb02a"/><path d="M3 14l8-6 6 4 10-9" fill="none" stroke="#6bb02a" stroke-width="2"/><path d="M23 3h5v5z" fill="#6bb02a"/></svg>Aenean placerat tortor ac dui luctus ut mattis est mollis. Donec blandit orci id velit cursus varius. Fusce quam ultrices a, vestibulum nec enim. Quisque imperdiet ultricies dolor in convallis.</p>
</div>
<div class="abs feature" style="left:520px">
  <h3>MULTI-USER CROP</h3>
  <p><svg width="28" height="28" viewBox="0 0 28 28"><rect x="3" y="5" width="20" height="14" fill="none" stroke="#6bb02a" stroke-width="2"/><path d="M9 15l3 3 6-7" fill="none" stroke="#6bb02a" stroke-width="2"/><ellipse cx="14" cy="24" rx="11" ry="2" fill="#6bb02a"/></svg>Donec hendrerit, felis in aliquet sodales, leo neque posuere arcu, sit amet sodales libero augue eget libero. Proin consequat odio eget ligula lobortis sodales. Suspendisse potenti.</p>
</div>

<div class="abs rule"></div>

<h2 class="abs section-title" style="left:18px;top:731px">WELCOME TO VERDANT FIELD FIBRES</h2>
<div class="abs welcome-photo" role="img" aria-label="Coastal valley landscape with a town by the sea"></div>
<p class="abs welcome-text">Jerta baditaut onquser kaytsrera untur magni dolores eoquie voluptate msequi nesciunt. Nique porroisquam esti dolorem ipsumquia dolorsitamet consectet rpisci velit.Bahseoquie voluptate msequisagni dolores nesciunt. Nique porrisquam estqui dolorem ipsumquia dolor adipisci unumquam labore esitamet consect olore nuaysas.</p>

<h2 class="abs section-title" style="left:330px;top:731px">PRODUCTS AND SERVICES</h2>
<ul class="abs services">
  <li>Lorem ipsum dolor sit amet</li>
  <li>Consectetur adipisicing elit</li>
  <li>Sed do eiusmod tempor</li>
  <li>Incididunt ut labore et dolore</li>
  <li>Magna aliqua. Ut enim ad</li>
  <li>Minim veniam, quis nostrud</li>
  <li>Exercitation ullamco laboris</li>
  <li>Nisi ut aliquip ex ea commodo</li>
</ul>

<h2 class="abs section-title" style="left:516px;top:731px">LATEST NEWS</h2>
<div class="abs news-item" style="top:757px">
  <div class="date"><b>27</b><i>JULY</i></div>
  <div class="news-body"><h4>Lorem ipsum dolor sit amet</h4><p>Lorem ipsum dolor sit amet, consectetur adipisicing elit, sed do.</p><a href="#">read more +</a></div>
</div>
<div class="abs dotted" style="top:816px"></div>
<div class="abs news-item" style="top:834px">
  <div class="date"><b>26</b><i>JUNE</i></div>
  <div class="news-body"><h4>Sed ut perspiciatis, unde</h4><p>Sed ut perspiciatis, unde omnis iste natus error sit voluptatem accusan</p><a href="#">read more +</a></div>
</div>
<div class="abs dotted" style="top:893px"></div>
<div class="abs more">MORE NEWS</div>

<footer class="abs footer"></footer>
<h2 class="abs footer-title" style="left:23px;top:1019px">NAVIGATION</h2>
<ul class="abs foot-links" style="left:23px;top:1046px"><li>Home</li><li>About Us</li><li>Production</li><li>Investors</li><li>Products</li></ul>
<ul class="abs foot-links" style="left:88px;top:1046px"><li>Sitemap</li><li>Contact Us</li><li>Terms of Use</li></ul>

<h2 class="abs footer-title" style="left:244px;top:1019px">EMAIL US</h2>
<div class="abs field" style="top:1048px">full name</div>
<div class="abs field" style="top:1070px">email address</div>
<div class="abs field" style="top:1092px;height:62px"></div>
<div class="abs send">send</div>

<h2 class="abs footer-title" style="left:525px;top:1019px">CONTACT US</h2>
<div class="abs social"><span></span><span></span><span></span><span></span><span></span></div>
<p class="abs sub-note">subscribe to our monthly newsletter<br>and get the best deals and discounts</p>
<div class="abs sub-field">enter email address</div>
<div class="abs sub-now">➤&nbsp; subscribe now</div>
<div class="abs phone"><svg width="20" height="20" viewBox="0 0 20 20"><circle cx="10" cy="10" r="8.5" fill="none" stroke="#c4a84a" stroke-width="1.4"/><path d="M7 5.5l2 2.5-1 1.2c.7 1.4 1.5 2.2 2.8 2.8l1.2-1 2.5 2-1 1.5c-3.5 0-7-3.5-7.5-7.5z" fill="#c4a84a"/></svg>0-98-7654321</div>

</body>
</html>
```